Create Brisk Lesson Studio a card design that will stick in the mind of prospects.

Brisk Lesson Studio specialises designs and produces training video, animation, illustration and text.

We need a card design that oozes class and leaves the prospect brimming with confidence.

The design will feature the Brisk Lesson Studio all black logo (uploaded). The design may also use the shade of orange from the orange version of the logo (uploaded). Note, just the color is to be used e.g. for the back of the card, not the orange logo itself.

The Brisk brand is about authenticity, quality, maturity and assurance. We are a safe buy when it comes to the prospects next project.

Target Market(s)

The primary target is training managers or others who are responsible for choosing to hire companies to produce their training media e.g. video. This will usually be a large spend so they need to have confidence.

Industry/Entity Type

Training

Contact Information for Business Card

FRONT:

Brisk Lesson Studio
Phone: 03 5172 4039
1st Floor, 418 Kellerby Road
Mt Ferncombe
VIC 3862
Australia
www.brisklesson.com.au

Lionel Petch
Founder and Lead Consultant
mobile: +61 3 0462 735 218
email: lionel@brisklesson.com.au

BACK:
Specialising in design and production of training:

video
animation
illustration
text

for delivery via internet, intranet and/or LMS.

Number of Pages Required

4 page

Font styles to use
Sans Serif

Requirements
Must have
• The black logo uploaded with the brief.
Nice to have
• The inclusion of the shade of orange found in the orange logo also uploaded with the brief. One example would be having the back of the card in this orange and using a white font for the text. But I want the designer to work this out.
Should not have
• No colours other than black and the orange included in the uploaded orange logo.

```html
<!DOCTYPE html>
<html lang="en">
<head>
<meta charset="utf-8">
<title>Brisk Lesson Studio – Business Card</title>
<link href="https://fonts.googleapis.com/css2?family=Arimo:wght@400;700&display=swap" rel="stylesheet">
<style>
  :root {
    --orange: #e5761a;
    --ink: #231f20;
    --white: #ffffff;
    --paper-bg: #dcdcdc;
    --ghost-light: #ececec;
    --ghost-dark: #4a4a4a;
    --edge-grey: #5a5a5a;
  }
  * { margin: 0; padding: 0; box-sizing: border-box; }
  html, body {
    width: 1200px; height: 1200px; overflow: hidden;
    background: var(--paper-bg);
    font-family: "Arimo", Arial, sans-serif;
  }
  .sheet { position: relative; width: 1200px; height: 1200px; }
  .card {
    position: absolute; left: 220px; width: 760px; height: 466px;
    overflow: hidden; background: var(--white);
    box-shadow: 0 14px 28px rgba(0,0,0,0.25);
  }
  .card--front { top: 94px; }
  .card--back { top: 640px; background: var(--ink); }
  .card__shape { position: absolute; inset: 0; width: 100%; height: 100%; }
  .abs { position: absolute; }

  /* front */
  .ghost-name {
    left: -8px; top: -6px; font-size: 128px; font-weight: 700;
    color: var(--ghost-light); letter-spacing: -2px; line-height: 1;
  }
  .person { left: 38px; top: 300px; }
  .person__name { font-size: 31px; font-weight: 700; color: var(--orange); line-height: 1; }
  .person__role { font-size: 15px; color: var(--ink); margin-top: 6px; }
  .contact { left: 38px; display: flex; align-items: center; font-size: 14px; color: var(--ink); }
  .contact--mobile { top: 376px; }
  .contact--email { top: 405px; }
  .contact__tag {
    width: 26px; height: 22px; background: var(--orange); color: var(--white);
    font-size: 13px; display: flex; align-items: center; justify-content: center;
    margin-right: 12px;
  }
  .brand-mark {
    left: 395px; width: 340px; top: 100px; text-align: center;
    font-size: 92px; font-weight: 700; color: var(--orange); line-height: 1;
  }
  .company {
    left: 395px; width: 340px; top: 306px; text-align: center; color: var(--white);
  }
  .company__name { font-size: 25px; font-weight: 700; letter-spacing: 0.3px; }
  .company__address { font-size: 14px; line-height: 18px; margin-top: 8px; }
  .company__links { font-size: 14px; line-height: 19px; margin-top: 9px; }
  .company__key { color: var(--orange); font-weight: 700; margin-right: 3px; }

  /* back */
  .ghost-mark {
    left: 20px; width: 330px; top: 180px; text-align: center;
    font-size: 100px; font-weight: 700; color: var(--ghost-dark); line-height: 1;
  }
  .services { left: 376px; width: 350px; top: 196px; text-align: center; color: var(--white); font-size: 14px; }
  .services__list {
    display: flex; justify-content: center; align-items: center;
    background: var(--ink); border-radius: 10px; height: 27px;
    margin: 8px 0; list-style: none;
  }
  .services__list li { padding: 0 13px; border-left: 1px solid var(--white); line-height: 16px; }
  .services__list li:first-child { border-left: none; }
</style>
</head>
<body>
<main class="sheet">

  <section class="card card--front" aria-label="Business card front">
    <svg class="card__shape" viewBox="0 0 896 550" preserveAspectRatio="none" aria-hidden="true">
      <path d="M562 0 Q282 275 537 550 L896 550 L896 0 Z" fill="var(--orange)"/>
      <path d="M571 0 Q290 275 546 550 L896 550 L896 0 Z" fill="var(--ink)"/>
    </svg>
    <div class="abs ghost-name" aria-hidden="true">Brisk</div>

    <div class="abs person">
      <h1 class="person__name">LIONEL PETCH</h1>
      <p class="person__role">Founder and Lead Consultant</p>
    </div>
    <p class="abs contact contact--mobile"><span class="contact__tag">m</span>+61 3 0462 735 218</p>
    <p class="abs contact contact--email"><span class="contact__tag">e</span>lionel@brisklesson.com.au</p>

    <div class="abs brand-mark">Brisk</div>
    <div class="abs company">
      <h2 class="company__name">BRISK LESSON STUDIO</h2>
      <p class="company__address">1st Floor, 418 Kellerby Road,<br>Mt Ferncombe, VIC 3862, Australia</p>
      <p class="company__links">
        <span class="company__key">p</span>03 5172 4039<br>
        <span class="company__key">w</span>www.brisklesson.com.au
      </p>
    </div>
  </section>

  <section class="card card--back" aria-label="Business card back">
    <svg class="card__shape" viewBox="0 0 896 550" preserveAspectRatio="none" aria-hidden="true">
      <path d="M561 0 Q293 275 536 550 L896 550 L896 0 Z" fill="var(--edge-grey)"/>
      <path d="M571 0 Q303 275 546 550 L896 550 L896 0 Z" fill="var(--orange)"/>
    </svg>
    <div class="abs ghost-mark" aria-hidden="true">Brisk</div>

    <div class="abs services">
      <p>Specialising in design and production of training:</p>
      <ul class="services__list">
        <li>video</li><li>animation</li><li>illustration</li><li>text</li>
      </ul>
      <p>for delivery via internet, intranet and/or LMS.</p>
    </div>
  </section>

</main>
</body>
</html>
```